Irrigation Business needs their business cards modernised and revamped

I would like to keep my current logo, colours and revamp the format of the card.

I would like the card to be clean yet important.

Im not sure if you include texture but i would like the named logo to be indented into the card etc.

show me something alive and free something thats clinical to the point yet has a feel of achievement. i would like people to go nice card.

Target Market(s)

high end clients, corporate, sports field manger, the guys that make the decisions

Industry/Entity Type

Business

Contact Information for Business Card

nformation to be included

Dorian Hesk (Director)
0487253916
dorian@tfcraft.biz
www.taddsfieldcrafts.com

instagram logo
google logo
facebook logo

Colors

Designer to choose colors to be used in the design.

Requirements
Nice to have
• indentations a really nice feel to the card good texture

```html
<!DOCTYPE html>
<html lang="en">
<head>
<meta charset="utf-8">
<title>Tadd's Field Crafts – Business Card</title>
<link href="https://fonts.googleapis.com/css2?family=Open+Sans:wght@400;600;700&display=swap" rel="stylesheet">
<style>
  :root {
    --backdrop: #1d1e21;
    --brand-blue: #2b5e9e;
    --brand-blue-deep: #234f88;
    --brand-blue-light: #3a6fb0;
    --card-white: #fbfbfb;
    --card-grey: #e9e9ea;
    --ink-dark: #2b2b2b;
    --ink-mid: #4a4a4a;
    --icon-blue: #2f8fcf;
  }
  * { margin: 0; padding: 0; box-sizing: border-box; }
  html, body {
    width: 1200px; height: 904px; overflow: hidden;
    background: var(--backdrop);
    font-family: "Open Sans", Arial, sans-serif;
  }
  .canvas { position: relative; width: 1200px; height: 904px; }

  .card {
    position: absolute;
    width: 620px; height: 354px;
    border-radius: 3px;
    box-shadow: 0 18px 40px rgba(0,0,0,.55);
    overflow: hidden;
  }

  /* Back of card */
  .card-back {
    left: 90px; top: 70px;
    background: linear-gradient(135deg, var(--brand-blue-light), var(--brand-blue) 55%, var(--brand-blue-deep));
    display: flex; flex-direction: column; align-items: center; justify-content: center; gap: 18px;
  }
  .back-mark {
    width: 110px; height: 110px; border-radius: 50%;
    background: rgba(255,255,255,.14);
  }
  .back-name {
    color: rgba(255,255,255,.85);
    font-weight: 700; font-size: 20px; letter-spacing: 3px; text-transform: uppercase;
  }

  /* Front of card */
  .card-front {
    left: 490px; top: 480px;
    background: linear-gradient(160deg, var(--card-grey), var(--card-white) 45%);
  }
  .brand {
    position: absolute; right: 44px; top: 42px;
    display: flex; align-items: center; gap: 12px;
  }
  .brand-dot { width: 52px; height: 52px; border-radius: 50%; background: var(--brand-blue); }
  .brand-name {
    color: var(--brand-blue);
    font-weight: 700; font-size: 24px; letter-spacing: .5px; text-transform: uppercase;
    line-height: 1;
  }

  .edge-tab {
    position: absolute; left: 0; top: 270px;
    width: 16px; height: 40px; background: var(--brand-blue);
  }
  .person { position: absolute; left: 34px; top: 266px; }
  .person-name { color: var(--brand-blue); font-weight: 700; font-size: 22px; line-height: 1.1; }
  .person-role { color: var(--ink-mid); font-size: 15px; margin-top: 2px; }

  .divider {
    position: absolute; left: 208px; top: 230px;
    width: 2px; height: 62px; background: var(--ink-dark);
  }
  .contacts {
    position: absolute; left: 228px; top: 222px;
    list-style: none;
  }
  .contacts li {
    display: flex; align-items: center; gap: 10px;
    color: var(--ink-dark); font-size: 15px; line-height: 24px;
  }
  .contacts svg { width: 14px; height: 14px; flex: none; }
</style>
</head>
<body>
<main class="canvas">

  <section class="card card-back" aria-label="Card back">
    <div class="back-mark"></div>
    <div class="back-name">Tadd's Field Crafts</div>
  </section>

  <section class="card card-front" aria-label="Card front">
    <div class="brand">
      <div class="brand-dot"></div>
      <div class="brand-name">Tadd's Field Crafts</div>
    </div>

    <div class="edge-tab"></div>
    <div class="person">
      <div class="person-name">Dorian Hesk</div>
      <div class="person-role">Director</div>
    </div>

    <div class="divider"></div>

    <ul class="contacts">
      <li>
        <svg viewBox="0 0 24 24" aria-hidden="true"><path fill="var(--icon-blue)" d="M6.6 10.8a15.1 15.1 0 0 0 6.6 6.6l2.2-2.2a1 1 0 0 1 1-.25 11.4 11.4 0 0 0 3.6.57 1 1 0 0 1 1 1V20a1 1 0 0 1-1 1A17 17 0 0 1 3 4a1 1 0 0 1 1-1h3.5a1 1 0 0 1 1 1c0 1.25.2 2.45.57 3.57a1 1 0 0 1-.25 1z"/></svg>
        0487253916
      </li>
      <li>
        <svg viewBox="0 0 24 24" aria-hidden="true"><rect x="2" y="5" width="20" height="14" rx="2" fill="var(--icon-blue)"/><path d="M3 6l9 7 9-7" fill="none" stroke="#fff" stroke-width="1.8"/></svg>
        dorian@tfcraft.biz
      </li>
      <li>
        <svg viewBox="0 0 24 24" aria-hidden="true"><circle cx="12" cy="12" r="10" fill="var(--icon-blue)"/><path d="M2 12h20M12 2c3 3 3 17 0 20M12 2c-3 3-3 17 0 20" fill="none" stroke="#fff" stroke-width="1.4"/></svg>
        www.taddsfieldcrafts.com
      </li>
    </ul>
  </section>

</main>
</body>
</html>
```